Flyer für einen Sanitär Heizungs Betrieb
Zielgruppe
Sanitär Heizungs Betrieb der den Fokus verstärkt auf den Service an Heizungsanlagen setzten will.
Der Flyer soll sowohl an Privathaushalte als auch an Hausverwaltungen gehen.
Er soll unsere Leistungen aufzeigen und einen guten ersten Eindruck vermitteln.
Aufgabenstellung
Anbei sende ich Themen die als Leistung aufgeführt werden, sowie Strichwort für einen Werbetext (kann gerne generiert werden ansonsten kommt er noch zum texter)

```html
<!DOCTYPE html>
<html lang="de">
<head>
<meta charset="utf-8">
<title>Nordbach GmbH – Flyer</title>
<link rel="stylesheet" href="https://fonts.googleapis.com/css2?family=Open+Sans:wght@400;600;700&display=swap">
<style>
  :root {
    --hero-dark: #2c2f33;
    --hero-mid: #4a4f54;
    --lawn: #3e4a2c;
    --accent-yellow: #f2c21b;
    --heading-blue: #1b74ba;
    --text-dark: #2a2a2a;
    --paper: #ffffff;
    --divider: #e6e6e6;
    --footer-bg: #2a2a2c;
    --footer-text: #ffffff;
  }
  * { margin: 0; padding: 0; box-sizing: border-box; }
  html, body { width: 844px; height: 1200px; overflow: hidden; background: var(--paper); }
  body { font-family: "Open Sans", Arial, sans-serif; color: var(--text-dark); }
  .flyer { position: relative; width: 844px; height: 1200px; }

  .hero { position: absolute; left: 0; top: 0; width: 844px; height: 541px; overflow: hidden; }
  .hero-photo {
    position: absolute; inset: 0;
    background:
      linear-gradient(180deg, rgba(30,32,36,0.55) 0%, rgba(30,32,36,0.45) 60%, rgba(30,32,36,0.55) 100%),
      linear-gradient(180deg, #5d6166 0%, var(--hero-mid) 45%, var(--hero-dark) 75%, var(--lawn) 100%);
  }
  .brand-box {
    position: absolute; left: 579px; top: 46px; width: 230px; height: 119px;
    background: var(--paper); display: flex; align-items: center; justify-content: center; gap: 9px;
  }
  .brand-mark { width: 16px; height: 16px; background: var(--accent-yellow); }
  .brand-name { font-weight: 700; font-size: 22px; color: var(--text-dark); }

  .hero-title {
    position: absolute; left: 49px; top: 170px; width: 540px;
    font-weight: 700; font-size: 35px; line-height: 48px; color: #fff; text-transform: uppercase;
  }
  .hero-rule { position: absolute; left: 49px; top: 340px; width: 217px; height: 3px; background: var(--accent-yellow); }
  .hero-lead {
    position: absolute; left: 49px; top: 372px; width: 621px;
    font-weight: 600; font-size: 21.5px; line-height: 28.6px; color: var(--accent-yellow);
  }

  .line { display: block; text-align: justify; text-align-last: justify; white-space: nowrap; }
  .line-end { display: block; text-align: left; white-space: nowrap; }

  .about { position: absolute; left: 49px; top: 568px; width: 750px; }
  .about-title { font-weight: 700; font-size: 31px; color: var(--heading-blue); line-height: 44px; margin-bottom: 10px; }
  .about-text { font-size: 17.4px; line-height: 27.3px; }
  .about-text strong { font-weight: 600; }

  .divider { position: absolute; left: 0; top: 957px; width: 844px; height: 10px; background: var(--divider); }
  .contact { position: absolute; left: 0; top: 967px; width: 844px; height: 233px; background: var(--footer-bg); color: var(--footer-text); }
  .location { position: absolute; top: 38px; font-size: 20.5px; line-height: 26.6px; font-style: normal; }
  .location-left { left: 49px; }
  .location-right { left: 462px; }
  .location-name { font-weight: 600; font-size: 21px; }
</style>
</head>
<body>
<div class="flyer">
  <header class="hero">
    <div class="hero-photo" role="img" aria-label="Foto eines modernen Einfamilienhauses mit Wärmepumpe im Garten bei Abenddämmerung"></div>
    <div class="brand-box"><span class="brand-mark"></span><span class="brand-name">Nordbach GmbH</span></div>
    <h1 class="hero-title">Herzlich Willkommen<br>beim Haus- und Wärme-<br>Technik Betrieb</h1>
    <div class="hero-rule"></div>
    <p class="hero-lead">
      <span class="line">Hier sind Sie richtig, wenn Sie nach einem erfahrenen</span>
      <span class="line">und zuverlässigen Haus und Wärme Technik Service</span>
      <span class="line">mit Kompetenz in Heizung, Badsanierung, Brenn-</span>
      <span class="line-end">stoffzellenheizung und Wärmepumpen suchen!</span>
    </p>
  </header>

  <section class="about">
    <h2 class="about-title">DAS SIND WIR</h2>
    <p class="about-text">
      <span class="line">Herzlich willkommen bei unserem Familienunternehmen im Kreis Ahrenfeld, das im</span>
      <span class="line">Jahr 2023 stolz sein 20-jähriges Jubiläum feiert! Unsere <strong>geschulten Fachkräfte</strong></span>
      <span class="line">stehen für eine Vielzahl von Leistungen bereit, darunter Wartung von Zentralheizun-</span>
      <span class="line">gen, Reparaturen von Heizungs- und Sanitäranlagen, Solaranlagenservice und vieles</span>
      <span class="line">mehr. Wir legen großen Wert auf <strong>gewissenhaftes und zielorientiertes Arbeiten</strong>,</span>
      <span class="line">und als eingetragener Meisterbetrieb der Innung Lindenberg garantieren wir <strong>höchste</strong></span>
      <span class="line"><strong>Qualität</strong>. Als Ausbildungsbetrieb sind wir stets bestrebt, Fachkompetenz und Inno-</span>
      <span class="line">vation zu fördern. Mit <strong>langjähriger Erfahrung</strong> im Umgang mit Privathaushalten und</span>
      <span class="line">Hausverwaltungen bieten wir Ihnen zuverlässige Dienstleistungen und einen <strong>erst-</strong></span>
      <span class="line"><strong>klassigen Service</strong>. Vertrauen Sie auf unser Engagement für Ihre Heizungs- und Sani-</span>
      <span class="line-end">täranliegen – wir freuen uns darauf, <strong>Sie persönlich</strong> betreuen zu dürfen.</span>
    </p>
  </section>

  <div class="divider"></div>
  <footer class="contact">
    <address class="location location-left">
      <div class="location-name">Standort Talbrunn an der Aue</div>
      Mühlgasse 12<br>72915 Talbrunn an der Aue<br>(0743) 48 20 91 7<br>info@nordbach-haustechnik.de
    </address>
    <address class="location location-right">
      <div class="location-name">Standort Hofstetten im Wald</div>
      Birkenallee 4<br>72915 Talbrunn an der Aue<br>(07452) 21 84 6<br>(07458) 53 17 29<br>info@nordbach-haustechnik.de
    </address>
  </footer>
</div>
</body>
</html>
```